Security Warning Sign

We have an existing sign that needs an update. I have attached a picture of the current square sign. We need to maintain the same wording. It needs to be professional and appropriate to attach to our customers fence. Also attached is a copy of our building sign which may lend some inspiration and hopefully the ai format will assist. The final sign will be 600mm x 600mmOur website is www.halvorngate.com.au

```html
<!DOCTYPE html>
<html lang="en">
<head>
<meta charset="utf-8">
<title>Halvorngate Security Services – Surveillance Warning Sign</title>
<link rel="stylesheet" href="https://fonts.googleapis.com/css2?family=Anton&family=Jost:wght@700&display=swap">
<style>
  :root {
    --sign-black: #000000;
    --sign-orange: #f48634;
    --sign-white: #ffffff;
    --panel-light: #f4f4f4;
    --panel-shade: #e2e2e2;
    --body-ink: #161616;
  }
  html, body {
    margin: 0;
    padding: 0;
    width: 1200px;
    height: 1200px;
    overflow: hidden;
    background: var(--sign-white);
  }
  .sign {
    display: block;
    width: 1200px;
    height: 1200px;
  }
  .headline {
    font-family: "Anton", "Impact", sans-serif;
    fill: var(--sign-orange);
  }
  .notice {
    font-family: "Jost", "Futura", sans-serif;
    font-weight: 700;
    fill: var(--body-ink);
  }
  .company-name {
    font-family: "Jost", "Futura", sans-serif;
    font-weight: 700;
    fill: var(--sign-white);
  }
  .phone {
    font-family: "Anton", "Impact", sans-serif;
    fill: var(--sign-white);
  }
  .header-band { fill: var(--sign-black); }
  .footer-brand { fill: var(--sign-black); }
  .footer-contact { fill: var(--sign-orange); }
  .brand-dot { fill: var(--sign-orange); }
</style>
</head>
<body>
<svg class="sign" viewBox="0 0 1200 1200" xmlns="http://www.w3.org/2000/svg" role="img" aria-label="Warning: electronic surveillance and recording devices installed in this area. Halvorngate Security Services, 1300 468 215">
  <defs>
    <linearGradient id="panelGradient" x1="0" y1="0" x2="1" y2="1">
      <stop offset="0" stop-color="var(--panel-shade)"/>
      <stop offset="0.45" stop-color="var(--panel-light)"/>
      <stop offset="1" stop-color="var(--panel-shade)"/>
    </linearGradient>
  </defs>

  <!-- Header band -->
  <rect class="header-band" x="0" y="0" width="1200" height="367"/>
  <text class="headline" x="600" y="308" text-anchor="middle" font-size="262" textLength="988" lengthAdjust="spacingAndGlyphs">WARNING</text>

  <!-- Notice panel -->
  <rect x="0" y="367" width="1200" height="597" fill="url(#panelGradient)" role="img" aria-label="Soft grey faceted background texture"/>
  <g class="notice" font-size="88" text-anchor="middle">
    <text x="600" y="496" textLength="540" lengthAdjust="spacingAndGlyphs">ELECTRONIC</text>
    <text x="600" y="595" textLength="887" lengthAdjust="spacingAndGlyphs">SURVEILLANCE AND</text>
    <text x="600" y="694" textLength="534" lengthAdjust="spacingAndGlyphs">RECORDING</text>
    <text x="600" y="792" textLength="864" lengthAdjust="spacingAndGlyphs">DEVICES INSTALLED</text>
    <text x="600" y="894" textLength="595" lengthAdjust="spacingAndGlyphs">IN THIS AREA</text>
  </g>

  <!-- Footer -->
  <rect class="footer-contact" x="0" y="964" width="1200" height="236"/>
  <polygon class="footer-brand" points="0,964 570,964 476,1200 0,1200"/>

  <circle class="brand-dot" cx="180" cy="1081" r="58"/>
  <g class="company-name" font-size="36">
    <text x="269" y="1056" textLength="247" lengthAdjust="spacingAndGlyphs">HALVORNGATE</text>
    <text x="269" y="1094" textLength="186" lengthAdjust="spacingAndGlyphs">SECURITY</text>
    <text x="269" y="1131" textLength="180" lengthAdjust="spacingAndGlyphs">SERVICES</text>
  </g>

  <text class="phone" x="840" y="1118" text-anchor="middle" font-size="100" textLength="507" lengthAdjust="spacingAndGlyphs">1300 468 215</text>
</svg>
</body>
</html>
```